Business card design for a content marketing agency

Need a business card design suitable for a digital marketing agency. Needs to be a bold and creative, high quality design that exudes expertise and professionalism, and instills in prospective new customers a sense of confidence that we are the right company to do business with. Specifications must meet PrintaLoom requirement for extra thick matte stock. Needs to incorporate logo, tagline, name, title, website url, address, city, state, zip code, and mobile number.. I spec'd s single side design but I'm to a double sided design if it's strong and compelling. I like the use of icons associated with contact info, but it's not a requirement. Mostly, the design needs to command attention because it's so good or unusual. I have all kinds of files in large thru small sizes in jpg andpgn. pick from what you need, and let me know if you have questions.

Target Market(s)

CEO, Mktg VP's and small to medium size tech and prof'l service businesses

Industry/Entity Type

Marketing

Contact Information for Business Card

Pedro Finch
Chief Executive Officer
487 Marrow Creek Lane
Sudbury, MA 01842
pedro@quenvelmedia.example
www.quenvelmedia.example
978-555-0163

Font styles to use
Sans Serif

Colors
0692cd
9bcb3c

Requirements
Must have
• Tagline is "Marketing That Customers Trust".
• Needs to be a bold and creative, high quality design that exudes expertise and professionalism, and instills in prospective new customers a sense of confidence that we are the right company to do business with. Specifications must meet PrintaLoom requirement for extra thick matte stock. Needs to incorporate logo, tagline, name, title, website url, address, city, state, zip code, and mobile number..
Nice to have
• I spec'd s single side design but I'm open to a double sided design if it's strong and compelling. I like the use of icons associated with contact info, but it's not a requirement.
Should not have
• Chose colors that are the same and/or compatible with colors in the logo

```html
<!DOCTYPE html>
<html lang="en">
<head>
<meta charset="utf-8">
<title>Quenvel Media – Business Card</title>
<link href="https://fonts.googleapis.com/css2?family=Open+Sans:wght@400;600&display=swap" rel="stylesheet">
<style>
  :root {
    --backdrop: #3b3b3b;
    --card-white: #f7f7f7;
    --brand-blue: #0a6cb5;
    --brand-blue-faint: rgba(255, 255, 255, 0.07);
    --ink: #1a1a1a;
    --ink-soft: #4a4a4a;
    --rule: #c9c9c9;
    --on-blue: #ffffff;
  }
  * { margin: 0; padding: 0; box-sizing: border-box; }
  html, body {
    width: 1200px; height: 750px; overflow: hidden;
    background: var(--backdrop);
    font-family: "Open Sans", sans-serif;
  }
  .card {
    position: absolute; top: 228px;
    width: 462px; height: 263px;
    overflow: hidden;
  }
  .card-front { left: 124px; background: var(--card-white); }
  .card-back { left: 618px; background: var(--brand-blue); }

  .wordmark {
    position: absolute; left: 0; right: 0; top: 64px;
    text-align: center;
    font-size: 36px; font-weight: 600; letter-spacing: -0.5px;
    color: var(--brand-blue);
  }
  .identity {
    position: absolute; right: 270px; top: 158px;
    text-align: right; white-space: nowrap;
  }
  .identity .person-name { font-size: 17px; font-weight: 600; color: var(--brand-blue); line-height: 22px; }
  .identity .person-title { font-size: 13px; color: var(--ink); line-height: 18px; }
  .divider {
    position: absolute; left: 208px; top: 140px;
    width: 1px; height: 76px; background: var(--rule);
  }
  .contact-list {
    position: absolute; left: 226px; top: 141px;
    list-style: none;
  }
  .contact-list li {
    display: flex; align-items: center; gap: 6px;
    font-size: 12px; line-height: 15px; color: var(--ink-soft);
    white-space: nowrap;
  }
  .contact-list li.continued { padding-left: 17px; }
  .contact-list svg { width: 11px; height: 11px; fill: var(--brand-blue); flex: none; }
  .edge-rule {
    position: absolute; left: 0; right: 0; top: 240px;
    height: 2px; background: var(--ink);
  }
  .edge-band {
    position: absolute; left: 0; right: 0; top: 244px; bottom: 0;
    background: var(--brand-blue);
  }
  .back-emblem {
    position: absolute; left: 160px; top: 0;
    width: 140px; height: 262px;
    border-radius: 60px 60px 20px 20px;
    background: linear-gradient(180deg, var(--brand-blue-faint), rgba(255,255,255,0.03));
  }
  .tagline {
    position: absolute; left: 0; right: 0; top: 219px;
    text-align: center;
    font-size: 14px; font-weight: 600; color: var(--on-blue);
  }
</style>
</head>
<body>
  <section class="card card-front">
    <div class="wordmark">Quenvel Media</div>
    <div class="identity">
      <div class="person-name">Pedro Finch</div>
      <div class="person-title">Chief Executive Officer</div>
    </div>
    <div class="divider"></div>
    <ul class="contact-list">
      <li>
        <svg viewBox="0 0 24 24" aria-hidden="true"><path d="M6.6 10.8a15.1 15.1 0 0 0 6.6 6.6l2.2-2.2c.3-.3.7-.4 1-.2 1.1.4 2.3.6 3.6.6.6 0 1 .4 1 1V20c0 .6-.4 1-1 1A17 17 0 0 1 3 4c0-.6.4-1 1-1h3.5c.6 0 1 .4 1 1 0 1.3.2 2.5.6 3.6.1.3 0 .7-.2 1z"/></svg>
        978.555.0163
      </li>
      <li>
        <svg viewBox="0 0 24 24" aria-hidden="true"><path d="M2 5h20v14H2z M2 5l10 8 10-8" fill="none" stroke="#0a6cb5" stroke-width="2.4"/></svg>
        pedro@quenvelmedia.example
      </li>
      <li>
        <svg viewBox="0 0 24 24" aria-hidden="true"><circle cx="12" cy="12" r="10"/><path d="M2 12h20M12 2c3 3 3 17 0 20M12 2c-3 3-3 17 0 20" fill="none" stroke="#f7f7f7" stroke-width="1.4"/></svg>
        www.quenvelmedia.example
      </li>
      <li>
        <svg viewBox="0 0 24 24" aria-hidden="true"><path d="M12 2a7 7 0 0 0-7 7c0 5 7 13 7 13s7-8 7-13a7 7 0 0 0-7-7zm0 9.5A2.5 2.5 0 1 1 12 6.5a2.5 2.5 0 0 1 0 5z"/></svg>
        487 Marrow Creek Lane
      </li>
      <li class="continued">Sudbury, MA 01842</li>
    </ul>
    <div class="edge-rule"></div>
    <div class="edge-band"></div>
  </section>

  <section class="card card-back">
    <div class="back-emblem" role="img" aria-label="Faint emblem of a lightbulb merging with a head in profile"></div>
    <div class="tagline">Marketing That Customers Trust</div>
  </section>
</body>
</html>
```